R Vandell tile

This add will be posted on a shopping cart at grocery store. I have limited space and need something to tie in all my info.Add will be top to bottom not horizontal
R. Vandell
Custom Tile & Marble
"4 generations of Service"
Our slogan is: creating the most beautiful living spaces
555-284-7160
www.vandelltile.example
email:rkhome19@mailbox.example
in business since 1975
We would like to use the color yellow in the design and R. Vandell has to be script font to match our trucks.

Target Market(s)

tile & marble flooring,walls, complete bathroom renovations new homes,remodels,

Industry/Entity Type

Shopping

Colors
ffc214
000000
b1b1b1
f37123

Requirements
Must have
• Would like yellow to be used sparingly all other colors are just a suggestion. Need R. Vandell To be in Script all other wording to be straight
Nice to have
• all contact info,other colors to tie into yellow

```html
<!DOCTYPE html>
<html lang="en">
<head>
<meta charset="UTF-8">
<title>R. Vandell Custom Tile &amp; Marble</title>
<link href="https://fonts.googleapis.com/css2?family=Great+Vibes&family=Montserrat:wght@400;500;600;700&display=swap" rel="stylesheet">
<style>
  :root {
    --yellow: #fbbf1d;
    --yellow-light: #fdd257;
    --charcoal: #2b2a29;
    --ink: #1f1e1d;
    --white: #ffffff;
    --gap: #f4f4f4;
    --tile-grey: #c9c8c4;
    --stone-grey: #a7a6a2;
  }
  * { margin: 0; padding: 0; box-sizing: border-box; }
  html, body { width: 818px; height: 1200px; overflow: hidden; background: var(--white); }
  .ad {
    position: relative;
    width: 818px;
    height: 1200px;
    background: var(--charcoal);
    font-family: "Montserrat", Arial, sans-serif;
  }
  .header {
    position: absolute; left: 0; top: 0; width: 818px; height: 400px;
    background: linear-gradient(180deg, var(--yellow-light) 0%, var(--yellow) 100%);
    text-align: center;
  }
  .brand-name {
    position: absolute; left: 0; right: 0; top: 78px;
    font-family: "Great Vibes", cursive;
    font-size: 150px; line-height: 1;
    color: var(--white); font-weight: 400;
  }
  .brand-trade {
    position: absolute; left: 0; right: 0; top: 250px;
    font-size: 35px; letter-spacing: 3px; font-weight: 500;
    color: var(--ink);
  }
  .slogan-band {
    position: absolute; left: 0; top: 400px; width: 818px; height: 96px;
    background: var(--charcoal);
    display: flex; align-items: center; justify-content: center;
    color: var(--white); font-size: 25px; font-weight: 400;
  }
  .gallery {
    position: absolute; left: 0; top: 496px; width: 818px; height: 326px;
    background: var(--gap);
  }
  .gallery .photo { position: absolute; top: 10px; height: 306px; }
  .photo-niche { left: 10px; width: 396px; background: linear-gradient(160deg, #dcdbd7, var(--tile-grey)); }
  .photo-shower { left: 414px; width: 394px; background: linear-gradient(200deg, #d2d1cd, var(--stone-grey)); }
  .footer {
    position: absolute; left: 0; top: 822px; width: 818px; height: 378px;
    background: var(--charcoal); color: var(--white); text-align: center;
  }
  .heritage {
    position: absolute; left: 0; right: 0; top: 62px;
    font-family: "Great Vibes", cursive; font-size: 64px; line-height: 1;
  }
  .since { position: absolute; left: 0; right: 0; top: 148px; font-size: 30px; }
  .contact { position: absolute; left: 60px; top: 250px; text-align: left; }
  .phone { font-size: 36px; font-weight: 700; color: var(--yellow); line-height: 1.2; }
  .email { font-size: 22px; margin-top: 8px; }
  .web-button {
    position: absolute; left: 479px; top: 258px; width: 329px; height: 64px;
    background: var(--yellow); color: var(--ink);
    display: flex; align-items: center; justify-content: center;
    font-size: 24px; font-weight: 600; letter-spacing: 1px;
  }
</style>
</head>
<body>
<div class="ad">
  <header class="header">
    <h1 class="brand-name">R. Vandell</h1>
    <p class="brand-trade">CUSTOM TILE &amp; MARBLE</p>
  </header>
  <div class="slogan-band">Creating the Most Beautiful Living Spaces</div>
  <section class="gallery">
    <div class="photo photo-niche" role="img" aria-label="White subway tile wall with a recessed shelf niche holding towels and bath products"></div>
    <div class="photo photo-shower" role="img" aria-label="Modern grey tiled shower with rain head, stone accent strip and built-in niche"></div>
  </section>
  <footer class="footer">
    <p class="heritage">Four Generations of Service</p>
    <p class="since">in business since 1975</p>
    <div class="contact">
      <p class="phone">555-284-7160</p>
      <p class="email">rkhome19@mailbox.example</p>
    </div>
    <div class="web-button">VANDELLTILE.EXAMPLE</div>
  </footer>
</div>
</body>
</html>
```